Board to put on a meditation centre - Lantern Grove

I need a board design for a new meditation centre based in Oslo which offers free courses in meditation and self-empowerment. The size of the board is width 374cm x height 104cm.  The name of the meditation centre together with subtitles should be on the board but also some elegant decoration that matches the theme (lantern grove/meditation).
Here is the website of the meditation centre to give you a feeling of it: https://lyktelundsenteret.no/
Good if you can use a blue color close to this one: rgb(37, 180, 193) as well as some brown/golden color (similar to the palette on the website).
On the board it should say:
Lyktelunden (in big letters, the rest is subtitles)
Meditasjon & Spirituell visdom
Kurs - Retreat - Dialog
lyktelundsenteret.no
The design should be very elegant and beautiful and the feeling should be of "An Lantern Grove". A logo is here attached and should be used but I need to get a better quality version of it, will upload that as soon as possible.

```html
<!DOCTYPE html>
<html lang="no">
<head>
<meta charset="utf-8">
<title>Lyktelunden</title>
<link href="https://fonts.googleapis.com/css2?family=Inter:wght@500;700&display=swap" rel="stylesheet">
<style>
  :root {
    --gold-deep: #b8894f;
    --gold-light: #ecd3a0;
    --sky: #a9d8e8;
    --sky-light: #cbe9f2;
    --panel: rgba(115, 115, 115, 0.5);
    --text: #ffffff;
    --accent: #e0283a;
  }
  html, body {
    margin: 0;
    padding: 0;
    overflow: hidden;
    background: #ffffff;
  }
  .board {
    position: relative;
    width: 1200px;
    height: 331px;
    overflow: hidden;
    font-family: "Inter", Arial, sans-serif;
    color: var(--text);
  }
  .backdrop {
    position: absolute;
    inset: 0;
  }
  .title-panel {
    position: absolute;
    left: 190px;
    top: 95px;
    width: 820px;
    height: 115px;
    background: var(--panel);
    display: flex;
    align-items: center;
    justify-content: center;
    gap: 26px;
  }
  .title-mark {
    width: 58px;
    height: 58px;
    border-radius: 50%;
    background: var(--accent);
    flex: none;
  }
  .title {
    margin: 0;
    font-size: 80px;
    font-weight: 700;
    letter-spacing: 1px;
    line-height: 1;
  }
  .subtitle {
    position: absolute;
    top: 271px;
    height: 40px;
    padding: 0 12px;
    background: var(--panel);
    display: flex;
    align-items: center;
    justify-content: center;
    font-size: 17px;
    font-weight: 500;
    letter-spacing: 0.3px;
    white-space: nowrap;
  }
  .subtitle--themes { left: 94px; width: 332px; }
  .subtitle--offer { left: 505px; width: 247px; }
  .subtitle--web { left: 826px; width: 251px; }
</style>
</head>
<body>
<div class="board">
  <svg class="backdrop" width="1200" height="331" viewBox="0 0 1200 331" role="img" aria-label="Sunlit meadow grass in golden light blending into a pale blue sky">
    <defs>
      <linearGradient id="meadow" x1="0" y1="0" x2="1" y2="1">
        <stop offset="0" stop-color="#e9cc92"/>
        <stop offset="0.45" stop-color="#d9b273"/>
        <stop offset="1" stop-color="var(--gold-deep)"/>
      </linearGradient>
      <linearGradient id="sky" x1="0" y1="0" x2="1" y2="0">
        <stop offset="0" stop-color="var(--sky-light)"/>
        <stop offset="1" stop-color="var(--sky)"/>
      </linearGradient>
    </defs>
    <rect width="1200" height="331" fill="url(#meadow)"/>
    <polygon points="740,0 1200,0 1200,331 600,331" fill="url(#sky)" opacity="0.95"/>
    <polygon points="740,0 780,0 640,331 600,331" fill="#ffffff" opacity="0.18"/>
  </svg>

  <div class="title-panel">
    <span class="title-mark" aria-hidden="true"></span>
    <h1 class="title">LYKTELUNDEN</h1>
  </div>

  <div class="subtitle subtitle--themes">MEDITASJON &amp; SPIRITUELL VISDOM</div>
  <div class="subtitle subtitle--offer">KURS - RETREAT - DIALOG</div>
  <div class="subtitle subtitle--web">LYKTELUNDSENTERET.NO</div>
</div>
</body>
</html>
```